A new art and beauty business needing a eCommerce design

I need an ecommerce design for my company that is based in Australia called 'Fern and Fable'. I make art and other products and would like the website to be an easy to use website, it must however, look modern and professional.

Could you please provide the finished product CODED with HTML etc. and ready to be used.

Colours can be chosen by the designer and are not limited in any way by our previous websites design.

I look forward to your submissions and will reward good work with our approval for payment.

If you would like further information you are welcome to ask.

Industry/Entity Type

Business

Contact Information for Business Card

Company Name: Fern and Fable

Owners Name: Darren Vollmacht

Address: 14 Copperfield Row
Tumbarra, NSW 2687
Australia

Phone: 0491 786 215

Email: contact@fern-andfable.com

Logo Text

Fern and Fable

```html
<!DOCTYPE html>
<html lang="en">
<head>
<meta charset="utf-8">
<title>Fern and Fable – Shop</title>
<link href="https://fonts.googleapis.com/css2?family=Open+Sans:wght@400;600;700&family=Great+Vibes&display=swap" rel="stylesheet">
<style>
  :root{
    --teal:#2bb3a6;
    --teal-dark:#22968b;
    --ink:#333333;
    --muted:#777777;
    --line:#dddddd;
    --bar:#3a3a3a;
    --paper:#ffffff;
    --soft:#f4f4f4;
  }
  *{box-sizing:border-box;margin:0;padding:0}
  html,body{width:811px;height:1200px;overflow:hidden;background:var(--paper)}
  body{font-family:"Open Sans",Arial,sans-serif;color:var(--ink);position:relative}
  .wrap{position:absolute;left:75px;width:660px}

  /* header */
  .site-header{top:18px;height:52px;display:flex;align-items:center;justify-content:space-between}
  .brand{display:flex;align-items:center;gap:8px;font-size:15px;font-weight:600;color:var(--teal)}
  .brand-dot{width:22px;height:22px;border-radius:50%;background:var(--teal)}
  .header-tools{display:flex;align-items:center;gap:6px}
  .search{width:160px;height:24px;border:1px solid var(--line);display:flex;align-items:center;justify-content:space-between;padding:0 6px;font-size:8px;color:#aaa}
  .cart{height:24px;padding:0 6px;background:var(--bar);color:#fff;font-size:8px;display:flex;align-items:center;gap:4px}

  /* nav */
  .main-nav{top:88px;height:28px;border-top:1px solid var(--line);border-bottom:1px solid var(--line);display:flex;justify-content:space-between;align-items:center;padding:0 4px}
  .main-nav a{font-size:8px;font-weight:600;color:var(--ink);text-decoration:none;letter-spacing:.3px}

  /* hero */
  .hero{top:126px;height:274px;background:linear-gradient(180deg,#c9c9c9 0%,#8f9592 45%,#3f8a84 70%,#6d7572 100%)}
  .hero-caption{position:absolute;left:0;right:0;top:130px;text-align:center;color:#fff}
  .hero-title{font-family:"Great Vibes",cursive;font-size:34px;line-height:1}
  .hero-text{font-size:7px;width:300px;margin:6px auto 8px;line-height:1.5}
  .btn{display:inline-block;font-size:7px;font-weight:700;color:#fff;padding:5px 12px;letter-spacing:.4px}
  .btn-dark{background:#2f3432}
  .btn-teal{background:var(--teal)}
  .hero-dots{position:absolute;right:12px;bottom:12px;display:flex;gap:4px}
  .hero-dots span{width:5px;height:5px;border-radius:50%;background:#fff}

  /* banners */
  .promo-row{top:410px;height:165px;display:flex;gap:10px}
  .promo{flex:1;position:relative}
  .promo-art{background:linear-gradient(135deg,#333 0%,#c0392b 30%,#e9c13a 50%,#3a78c2 70%,#6a3f8f 100%)}
  .promo-goods{background:linear-gradient(160deg,#e8e8e8 0%,#b7b4c4 45%,#5b2f9a 75%,#c9c9cf 100%)}
  .promo-caption{position:absolute;left:12px;top:40px;width:160px;color:#fff}
  .promo-title{font-family:"Great Vibes",cursive;font-size:34px;line-height:1}
  .promo-text{font-size:7px;line-height:1.5;margin:3px 0 8px}

  /* featured */
  .featured-head{top:606px;height:28px;border-top:1px solid var(--line);display:flex;justify-content:space-between;align-items:center;padding-top:12px}
  .featured-head h2{font-size:15px;font-weight:600}
  .arrows{display:flex;gap:3px}
  .arrows span{width:18px;height:18px;background:var(--teal);display:flex;align-items:center;justify-content:center}
  .arrows span:last-child{background:var(--bar)}
  .products{top:650px;display:flex;justify-content:space-between}
  .product{width:152px}
  .product-image{height:130px;border:1px solid var(--line)}
  .p1{background:radial-gradient(circle at 40% 45%,#f3d23a 0,#e44c2f 25%,#3d8fd6 45%,#ffffff 70%)}
  .p2{background:radial-gradient(circle at 50% 50%,#e8e2ea 0,#f6f6f6 60%,#ffffff 100%)}
  .p3{background:linear-gradient(135deg,#fff 0%,#e62f8a 30%,#2a58c8 55%,#f3b6d0 80%,#fff 100%)}
  .p4{background:linear-gradient(135deg,#f4e34a 0%,#7cc04a 35%,#e2438f 65%,#f6ef7a 100%)}
  .product-title{font-size:8px;margin:6px 0}
  .buy-row{display:flex;align-items:center;gap:4px}
  .qty{display:flex;border:1px solid var(--line);height:20px}
  .qty span{width:18px;display:flex;align-items:center;justify-content:center;font-size:8px;color:var(--muted)}
  .qty span:nth-child(2){width:28px;border-left:1px solid var(--line);border-right:1px solid var(--line)}
  .price{margin-left:auto;background:var(--teal);color:#fff;font-size:9px;font-weight:700;padding:0 8px;height:20px;display:flex;align-items:center}

  /* footer */
  .site-footer{top:930px;height:190px;border-top:1px solid var(--line);display:flex;gap:20px;padding-top:12px}
  .foot-col{width:142px}
  .foot-col h3{font-size:9px;font-weight:700;letter-spacing:.3px;margin-bottom:10px}
  .foot-col li{list-style:none;font-size:7px;color:var(--muted);line-height:14px}
  .newsletter{width:170px}
  .email-field{height:22px;border:1px solid var(--line);font-size:7px;color:#999;display:flex;align-items:center;justify-content:center}
  .subscribe{height:22px;margin-top:6px;background:var(--teal);color:#fff;font-size:7px;font-weight:700;display:flex;align-items:center;justify-content:center;letter-spacing:.4px}
  .newsletter h3.keep{margin-top:14px}
  .social{display:flex;gap:5px}
  .social span{width:20px;height:20px;background:var(--teal)}
  .social span:nth-child(even){background:var(--teal-dark)}

  .legal-bar{position:absolute;left:75px;width:660px;top:1128px;height:34px;background:var(--bar);color:#ccc;font-size:6px;display:flex;align-items:center;justify-content:center}
</style>
</head>
<body>

<header class="wrap site-header">
  <div class="brand"><span class="brand-dot"></span>Fern and Fable</div>
  <div class="header-tools">
    <div class="search">Search your product here
      <svg width="10" height="10" viewBox="0 0 10 10"><circle cx="4" cy="4" r="3" fill="none" stroke="#2bb3a6" stroke-width="1.2"/><line x1="6.2" y1="6.2" x2="9" y2="9" stroke="#2bb3a6" stroke-width="1.2"/></svg>
    </div>
    <div class="cart">Cart
      <svg width="12" height="10" viewBox="0 0 12 10"><path d="M0 1h2l1.5 6h6.5l1.5-4.5H3" fill="none" stroke="#fff" stroke-width="1"/><circle cx="4.5" cy="9" r=".9" fill="#fff"/><circle cx="9" cy="9" r=".9" fill="#fff"/></svg>
    </div>
  </div>
</header>

<nav class="wrap main-nav">
  <a href="#">HOME</a><a href="#">ABOUT US</a><a href="#">PRODUCTS</a><a href="#">SALE</a><a href="#">BRANDS</a><a href="#">QUICK ORDER</a><a href="#">TERMS OF SERVICE</a><a href="#">CONTACT</a>
</nav>

<section class="wrap hero" role="img" aria-label="Two teal scented candles in glass jars on a table">
  <div class="hero-caption">
    <div class="hero-title">Fern &amp; Fable</div>
    <p class="hero-text">Handmade candles, prints and beauty goods crafted in small batches in Australia. Browse the new season collection today and find a gift for someone special.</p>
    <span class="btn btn-dark">SHOP NOW</span>
  </div>
  <div class="hero-dots"><span></span><span></span><span></span><span></span></div>
</section>

<section class="wrap promo-row">
  <div class="promo promo-art" role="img" aria-label="Colourful abstract paint pour artwork">
    <div class="promo-caption">
      <div class="promo-title">Art</div>
      <p class="promo-text">Bold abstract pieces poured by hand on canvas and board.</p>
      <span class="btn btn-teal">SHOP NOW</span>
    </div>
  </div>
  <div class="promo promo-goods" role="img" aria-label="Purple candles in glass jars">
    <div class="promo-caption">
      <div class="promo-title">Other Products</div>
      <p class="promo-text">Soaps, candles and gifts made with care from natural ingredients.</p>
      <span class="btn btn-teal">SHOP NOW</span>
    </div>
  </div>
</section>

<div class="wrap featured-head">
  <h2>Featured Products</h2>
  <div class="arrows">
    <span><svg width="8" height="8" viewBox="0 0 8 8"><path d="M5 1L2 4l3 3" fill="none" stroke="#fff" stroke-width="1.4"/></svg></span>
    <span><svg width="8" height="8" viewBox="0 0 8 8"><path d="M3 1l3 3-3 3" fill="none" stroke="#fff" stroke-width="1.4"/></svg></span>
  </div>
</div>

<section class="wrap products">
  <article class="product">
    <div class="product-image p1" role="img" aria-label="Rainbow paint splash artwork"></div>
    <p class="product-title">Product Title here</p>
    <div class="buy-row"><div class="qty"><span>−</span><span>50</span><span>+</span></div><span class="price">$50.00</span></div>
  </article>
  <article class="product">
    <div class="product-image p2" role="img" aria-label="White speckled abstract artwork"></div>
    <p class="product-title">Product Title here</p>
    <div class="buy-row"><div class="qty"><span>−</span><span>50</span><span>+</span></div><span class="price">$50.00</span></div>
  </article>
  <article class="product">
    <div class="product-image p3" role="img" aria-label="Pink and blue paint pour artwork"></div>
    <p class="product-title">Product Title here</p>
    <div class="buy-row"><div class="qty"><span>−</span><span>50</span><span>+</span></div><span class="price">$50.00</span></div>
  </article>
  <article class="product">
    <div class="product-image p4" role="img" aria-label="Yellow, green and pink abstract artwork"></div>
    <p class="product-title">Product Title here</p>
    <div class="buy-row"><div class="qty"><span>−</span><span>50</span><span>+</span></div><span class="price">$50.00</span></div>
  </article>
</section>

<footer class="wrap site-footer">
  <div class="foot-col">
    <h3>SHOPPING WITH US</h3>
    <ul><li>Why shop with us?</li><li>How it works</li><li>Delivery</li><li>Returns</li><li>Where's my order</li><li>Contact &amp; help</li><li>Wedding list</li><li>Gift vouchers</li></ul>
  </div>
  <div class="foot-col">
    <h3>ABOUT US</h3>
    <ul><li>Our story</li><li>Customer contact</li><li>Awards</li><li>Press room</li><li>Work with us</li><li>Terms &amp; conditions</li><li>Privacy &amp; cookies</li></ul>
  </div>
  <div class="foot-col">
    <h3>SELLING WITH US</h3>
    <ul><li>Why join?</li><li>Fees</li><li>Apply to sell with us</li><li>Affiliates</li></ul>
  </div>
  <div class="newsletter">
    <h3 class="foot-col" style="width:auto">SIGNUP NEWSLETTER</h3>
    <div class="email-field">EMAIL ADDRESS</div>
    <div class="subscribe">SUBSCRIBE NOW</div>
    <h3 class="foot-col keep" style="width:auto">KEEP IN TOUCH</h3>
    <div class="social"><span></span><span></span><span></span><span></span><span></span></div>
  </div>
</footer>

<div class="legal-bar">Copyright © 2015 - Fern &amp; Fable | All right reserved</div>

</body>
</html>
```